Talvex Engineering Business card Design

We need to make business cards for our NDT and inspection company. The company is called Talvex Engineering. We want a professional modern feel business card. We have just completed the remaking of our website and would like to have business cards with the same feel and colours. The final design should communicate professionalism and cutting edge tech.

Target Market(s)

We sell to B2B Business clients. Our customer is an engineer or decision maker in the mechanical engineering / Oil and gas field.

Contact Information for Business Card

Please see the current business cards that we have uploaded to get the details. You can also look at our Website www.talvex-eng.example for more.

Requirements
Must have
• Less is more
Nice to have
• Less is more

```html
<!DOCTYPE html>
<html lang="en">
<head>
<meta charset="utf-8">
<title>Talvex Engineering – Business Card</title>
<link href="https://fonts.googleapis.com/css2?family=Poppins:wght@400;500;600&display=swap" rel="stylesheet">
<style>
  :root{
    --navy:#263a78;
    --red:#b31f2a;
    --paper:#ffffff;
    --mist:#eceef3;
    --ground:#2b2b2d;
    --ink:#263a78;
  }
  *{box-sizing:border-box;margin:0;padding:0}
  html,body{width:1200px;height:900px;overflow:hidden;background:var(--ground);font-family:"Poppins",sans-serif;color:var(--ink)}
  .card{position:absolute;left:250px;width:700px;height:400px;background:var(--paper);overflow:hidden;box-shadow:0 12px 30px rgba(0,0,0,.45)}
  .card--front{top:25px}
  .card--back{top:475px}

  /* front */
  .front-art{position:absolute;inset:0}
  .wordmark{position:absolute;left:70px;top:48px;color:var(--navy);font-weight:500;line-height:1}
  .wordmark__main{display:block;font-size:56px;letter-spacing:4px}
  .wordmark__sub{display:block;font-size:17px;letter-spacing:12.5px;margin-top:8px;padding-left:4px}
  .holder{position:absolute;left:60px;top:150px;font-size:20px;font-weight:500;text-transform:uppercase;letter-spacing:.5px}
  .holder__first{color:var(--navy)}
  .holder__rest{color:var(--red)}
  .rule{position:absolute;left:50px;top:185px;width:405px;height:1.5px;background:var(--navy)}
  .contacts{position:absolute;left:50px;top:198px;list-style:none;font-size:15px;line-height:24px;color:var(--navy)}
  .contacts li{display:flex;align-items:center;gap:9px}
  .dot-icon{width:16px;height:16px;border-radius:50%;background:var(--red);display:inline-flex;align-items:center;justify-content:center}
  .social{position:absolute;left:50px;top:312px;display:flex;align-items:center;gap:8px;color:#fff;font-size:14px}
  .social__mark{width:10px;height:10px;background:#fff;border-radius:50%}
  .address{position:absolute;left:440px;top:285px;font-size:15px;line-height:22px;color:var(--navy)}
  .address__line{display:flex;align-items:center;gap:8px}
  .address__line--indent{padding-left:24px}

  /* back */
  .services{position:absolute;left:48px;top:34px;list-style:none;font-size:15px;font-weight:500;color:var(--navy);line-height:24.5px}
  .services li{display:flex;align-items:center;gap:12px}
  .services .gap{margin-top:12px}
  .ring{width:13px;height:13px;border-radius:50%;border:2px solid var(--red);display:inline-flex;align-items:center;justify-content:center;flex:none}
  .ring::after{content:"";width:5px;height:5px;border-radius:50%;background:var(--red)}
  .services .lead{font-size:17px}
  .brand-side{position:absolute;right:0;top:0;width:260px;height:400px}
  .brand-side__badge{position:absolute;left:70px;top:48px;width:92px;height:92px;border-radius:50%;background:var(--paper);display:flex;align-items:center;justify-content:center;box-shadow:0 0 0 1px #d9dbe2}
  .brand-side__badge span{width:74px;height:74px;border-radius:50%;background:var(--navy)}
  .vertical-mark{position:absolute;left:146px;top:160px;transform-origin:0 0;transform:rotate(90deg);white-space:nowrap;color:var(--navy);font-weight:500;line-height:1}
  .vertical-mark__name{display:block;font-size:34px;letter-spacing:3px}
  .vertical-mark__sub{display:block;font-size:12px;letter-spacing:6.6px;margin-top:5px}
  .vertical-mark__url{display:block;font-size:9.5px;letter-spacing:1.6px;margin-top:6px}
</style>
</head>
<body>

<section class="card card--front" aria-label="Business card front">
  <svg class="front-art" width="700" height="400" viewBox="0 0 700 400">
    <circle cx="560" cy="185" r="150" fill="none" stroke="var(--mist)" stroke-width="28"/>
    <polygon points="0,290 330,290 345,330 0,330" fill="var(--red)"/>
    <polygon points="0,330 345,330 560,400 0,400" fill="var(--navy)"/>
    <polygon points="345,330 420,330 700,400 560,400" fill="var(--navy)"/>
    <polygon points="600,372 700,372 700,400" fill="var(--red)"/>
    <circle cx="555" cy="185" r="86" fill="#fff" stroke="#d9dbe2" stroke-width="2"/>
    <circle cx="555" cy="185" r="76" fill="var(--navy)"/>
  </svg>

  <div class="wordmark">
    <span class="wordmark__main">TALVEX</span>
    <span class="wordmark__sub">ENGINEERING</span>
  </div>

  <p class="holder"><span class="holder__first">Harlow,</span> <span class="holder__rest">Peter Nandi</span></p>
  <div class="rule"></div>

  <ul class="contacts">
    <li><span class="dot-icon"><svg width="9" height="9" viewBox="0 0 10 10"><path d="M2 1l2 2-1 1.2c.6 1.2 1.5 2.1 2.8 2.8L7 6l2 2-1.3 1.3C4.5 9 1 5.5.7 2.3z" fill="#fff"/></svg></span>+254 20 555 0142/3</li>
    <li><span class="dot-icon"><svg width="9" height="7" viewBox="0 0 10 7"><rect x=".5" y=".5" width="9" height="6" fill="none" stroke="#fff"/><path d="M.5.5L5 4 9.5.5" fill="none" stroke="#fff"/></svg></span>info@talvex-eng.example</li>
    <li><span class="dot-icon"><svg width="10" height="10" viewBox="0 0 10 10"><circle cx="5" cy="5" r="4" fill="none" stroke="#fff"/><path d="M1 5h8M5 1v8" stroke="#fff"/></svg></span>www.talvex-eng.example</li>
  </ul>

  <div class="social">Find us on <span class="social__mark"></span><span class="social__mark"></span></div>

  <div class="address">
    <p class="address__line"><span class="dot-icon"><svg width="8" height="10" viewBox="0 0 8 10"><path d="M4 10S0 5.5 0 3.6a4 4 0 018 0C8 5.5 4 10 4 10z" fill="#fff"/><circle cx="4" cy="3.7" r="1.4" fill="var(--red)"/></svg></span>P.O. BOX 40512-80100</p>
    <p class="address__line address__line--indent">Mombasa Kenya</p>
  </div>
</section>

<section class="card card--back" aria-label="Business card back">
  <ul class="services">
    <li><span class="ring"></span>API 653 Tank Inspections</li>
    <li><span class="ring"></span>API 570 Pipeline Inspections</li>
    <li><span class="ring"></span>API 510 Pressure Vessel Inspections</li>
    <li><span class="ring"></span>Welding Inspections</li>
    <li><span class="ring"></span>Electrical Inspections</li>
    <li><span class="ring"></span>OCTG Inspections</li>
    <li><span class="ring"></span>Lifting Equipment Inspections</li>
    <li class="gap lead"><span class="ring"></span>Non-Destructive Testing</li>
    <li><span class="ring"></span>UT / PT / MT / RT / VT</li>
    <li class="lead"><span class="ring"></span>Advanced NDT</li>
    <li><span class="ring"></span>PAUT / MFL / ILI</li>
    <li class="gap lead"><span class="ring"></span>Engineering Projects</li>
  </ul>

  <div class="brand-side">
    <svg width="260" height="400" viewBox="0 0 260 400">
      <defs>
        <linearGradient id="sideFade" x1="0" y1="0" x2="1" y2="1">
          <stop offset="0" stop-color="var(--navy)"/>
          <stop offset="1" stop-color="var(--red)"/>
        </linearGradient>
      </defs>
      <path d="M20 0H260V400H200C200 350 160 320 160 270V200C160 165 120 160 95 135C60 100 45 40 20 0Z" fill="url(#sideFade)"/>
    </svg>
    <div class="brand-side__badge"><span></span></div>
    <div class="vertical-mark">
      <span class="vertical-mark__name">TALVEX</span>
      <span class="vertical-mark__sub">ENGINEERING</span>
      <span class="vertical-mark__url">WWW.TALVEX-ENG.EXAMPLE</span>
    </div>
  </div>
</section>

</body>
</html>
```